Homemaking training schools needs a Business Card design

Designer, Hello!

No special requirements, good-looking enough.
--------------------------------------------------------------------------

Name: Marcus Liao
Chairman
Tel: 0574-57418263
Mobile: 13852247106
Email: kelvory@mailpond.com
Web: www.tqb2031.com
Add: No.258, LinfengJie, DaoyueQu, Ningbo, Zhejiang

LOGO
Ningbo TQB Homemaking Training School

Target Market(s)

pregnant women, mothers, infants, the elderly and families, including cleaning, cooking, nursing training.

Industry/Entity Type

Business

Contact Information for Business Card

Name: Marcus Liao
Chairman
Tel: 0574-57418263
Mobile: 13852247106
Email: kelvory@mailpond.com
Web: www.tqb2031.com

LOGO

Font styles to use
Serif
Sans Serif
Decorative

Requirements
Nice to have
• Feels: clean, specifications, safety, comfort, warmth and happiness.

```html
<!DOCTYPE html>
<html lang="en">
<head>
<meta charset="utf-8">
<title>TanQiBao Business Card</title>
<link rel="stylesheet" href="https://fonts.googleapis.com/css2?family=Open+Sans:wght@400;600;700&display=swap">
<style>
:root{
  --brand-blue:#1f73b7;
  --brand-blue-soft:#6fa6d6;
  --brand-pink:#e6007e;
  --ink-grey:#4d4d4d;
  --card-white:#ffffff;
  --card-edge:#e4e4e4;
  --stage:#ecebe8;
}
*{box-sizing:border-box;margin:0;padding:0}
html,body{width:1200px;height:950px;overflow:hidden}
body{background:var(--stage);font-family:"Open Sans",Arial,sans-serif;position:relative}
.card{
  position:absolute;left:250px;width:700px;height:400px;
  background:linear-gradient(135deg,var(--card-white) 0%,#f3f3f3 100%);
  border:1px solid var(--card-edge);
  box-shadow:0 10px 28px rgba(0,0,0,.14);
  overflow:hidden;
}
.card--back{top:50px}
.card--front{top:500px}
.wordmark{display:flex;align-items:center;gap:14px;color:var(--brand-blue);font-weight:700;letter-spacing:.5px;white-space:nowrap}
.wordmark__dot{width:22px;height:22px;border-radius:50%;background:var(--brand-pink);flex:none}
.card--back .wordmark{position:absolute;left:50%;top:50%;transform:translate(-50%,-50%);font-size:64px}
.card--back .wordmark__dot{width:30px;height:30px}
.card--front .wordmark{position:absolute;left:300px;bottom:48px;font-size:52px}
.brand-symbol-area{
  position:absolute;left:40px;top:40px;width:210px;height:320px;border-radius:18px;
  background:linear-gradient(160deg,var(--brand-blue-soft) 0%,var(--brand-blue) 100%);
}
.contact{position:absolute;left:300px;top:48px;color:var(--ink-grey);font-size:19px;line-height:1.35}
.contact__name{color:var(--brand-blue);font-weight:700;font-size:25px;line-height:1.1}
.contact__title{color:var(--brand-pink);font-size:17px;margin-bottom:12px}
.contact__address{margin-bottom:4px}
.contact__line{display:flex;align-items:center;gap:10px}
.contact__icon{width:17px;height:17px;flex:none;fill:var(--brand-blue)}
</style>
</head>
<body>
  <section class="card card--back" aria-label="Card back">
    <div class="wordmark"><span class="wordmark__dot"></span><span>TanQiBao</span></div>
  </section>

  <section class="card card--front" aria-label="Card front">
    <div class="brand-symbol-area" role="img" aria-label="Large brand symbol area"></div>
    <div class="contact">
      <p class="contact__name">Marcus Liao</p>
      <p class="contact__title">Chairman</p>
      <p class="contact__address">No.258, LinfengJie<br>DaoyueQu, Ningbo, Zhejiang</p>
      <p class="contact__line">
        <svg class="contact__icon" viewBox="0 0 24 24" aria-hidden="true"><path d="M6.6 10.8a15 15 0 0 0 6.6 6.6l2.2-2.2c.3-.3.7-.4 1-.2 1.1.4 2.3.6 3.6.6.6 0 1 .4 1 1V20c0 .6-.4 1-1 1A17 17 0 0 1 3 4c0-.6.4-1 1-1h3.5c.6 0 1 .4 1 1 0 1.3.2 2.5.6 3.6.1.3 0 .7-.2 1z"/></svg>
        <span>0574-57418263</span></p>
      <p class="contact__line">
        <svg class="contact__icon" viewBox="0 0 24 24" aria-hidden="true"><path d="M7 1h10a2 2 0 0 1 2 2v18a2 2 0 0 1-2 2H7a2 2 0 0 1-2-2V3a2 2 0 0 1 2-2zm0 3v14h10V4zm5 15.5a1 1 0 1 0 0 2 1 1 0 0 0 0-2z"/></svg>
        <span>13852247106</span></p>
      <p class="contact__line">
        <svg class="contact__icon" viewBox="0 0 24 24" aria-hidden="true"><path d="M2 5h20v14H2zm2 2v.5l8 5 8-5V7zm0 2.8V17h16V9.8l-8 5z"/></svg>
        <span>kelvory@mailpond.com</span></p>
      <p class="contact__line">
        <svg class="contact__icon" viewBox="0 0 24 24" aria-hidden="true"><path d="M12 2a10 10 0 1 0 0 20 10 10 0 0 0 0-20zm6.9 6h-3a15 15 0 0 0-1.3-3.9A8 8 0 0 1 18.9 8zM12 4c.8 1.2 1.5 2.5 1.9 4h-3.8c.4-1.5 1.1-2.8 1.9-4zM4.3 14a8 8 0 0 1 0-4h3.4a16 16 0 0 0 0 4zm.8 2h3a15 15 0 0 0 1.3 3.9A8 8 0 0 1 5.1 16zm3-8h-3a8 8 0 0 1 4.3-3.9C8.8 5.3 8.4 6.6 8.1 8zM12 20c-.8-1.2-1.5-2.5-1.9-4h3.8c-.4 1.5-1.1 2.8-1.9 4zm2.3-6H9.7a14 14 0 0 1 0-4h4.6a14 14 0 0 1 0 4zm.3 5.9c.6-1.2 1-2.5 1.3-3.9h3a8 8 0 0 1-4.3 3.9zm1.7-5.9a16 16 0 0 0 0-4h3.4a8 8 0 0 1 0 4z"/></svg>
        <span>www.tqb2031.com</span></p>
    </div>
    <div class="wordmark"><span class="wordmark__dot"></span><span>TanQiBao</span></div>
  </section>
</body>
</html>
```